KT Design Business Card

I would like a business card similar to this
https://www.artquorra.com/design/8173920
with my info and a picture of my rifle. You can use something like this
https://www.snaplirra.com/pin/381926405572018843/visual-search/?cropSource=6&h=476&w=268&x=12&y=12
or
https://www.snaplirra.com/pin/219604837751093468/

I have a logo, it is a shepperds staff. I build custom rifles and do Law Enforcement sales. Some where on the card it needs to say something like, "Custom AR's built correctly", "All rifles come with honed uppers and bedded barrels", "All rifles are fully tested and come with a 3 shot card", "Law Enforcement models are available", "Tactical Equipment Consulting", "One stop shop for all tactical equipment"

Business Name: KT Design LLC
Name: Brent Hollis
Phone: (555) 614-2980
Email: brent.ktdesign@mailbriq.com
Address: 3082 Tamblin Ct., Brookvale, TN, 29815

Just use the concept of the staff in the attachments the other stuff is not related

```html
<!DOCTYPE html>
<html lang="en">
<head>
<meta charset="utf-8">
<title>KT Design Business Card</title>
<link href="https://fonts.googleapis.com/css2?family=Roboto:wght@400;500;700&display=swap" rel="stylesheet">
<style>
  :root {
    --page: #e9e7e4;
    --card-dark: #1b1b1b;
    --card-dark-edge: #262626;
    --card-light: #ffffff;
    --ink: #1c1c1c;
    --ink-soft: #4a4a4a;
    --ink-on-dark: #f2f2f2;
    --photo-a: #55585e;
    --photo-b: #2e2f32;
    --photo-c: #6f6a5e;
  }
  * { box-sizing: border-box; margin: 0; padding: 0; }
  html, body { width: 1200px; height: 960px; overflow: hidden; }
  body {
    background: var(--page);
    font-family: "Roboto", Arial, sans-serif;
    display: flex;
    flex-direction: column;
    align-items: center;
    justify-content: center;
    gap: 40px;
  }
  .card {
    width: 700px;
    height: 400px;
    position: relative;
    overflow: hidden;
    box-shadow: 0 8px 24px rgba(0,0,0,0.18);
  }

  /* Back side */
  .card--back {
    background: linear-gradient(135deg, var(--card-dark-edge), var(--card-dark) 60%);
    color: var(--ink-on-dark);
  }
  .rifle-photo {
    position: absolute;
    left: 60px;
    top: 20px;
    width: 230px;
    height: 360px;
    background: linear-gradient(160deg, var(--photo-a) 0%, var(--photo-b) 50%, var(--photo-c) 100%);
    opacity: 0.85;
  }
  .back-content {
    position: absolute;
    right: 40px;
    top: 70px;
    text-align: right;
  }
  .brand {
    font-weight: 700;
    letter-spacing: 0.5px;
    display: inline-flex;
    align-items: center;
    gap: 10px;
  }
  .brand-mark {
    width: 12px;
    height: 12px;
    background: currentColor;
  }
  .card--back .brand { font-size: 34px; margin-bottom: 22px; }
  .features { list-style: none; font-size: 15px; line-height: 1.55; }
  .features li::after { content: " \2022"; }

  /* Front side */
  .card--front { background: var(--card-light); color: var(--ink); }
  .holder-name {
    position: absolute;
    top: 34px;
    right: 40px;
    font-size: 28px;
    font-weight: 700;
    letter-spacing: 0.3px;
  }
  .name-tab {
    position: absolute;
    top: 28px;
    right: 0;
    width: 14px;
    height: 42px;
    background: var(--ink);
  }
  .contact {
    position: absolute;
    right: 40px;
    top: 150px;
    text-align: right;
    font-size: 15px;
    line-height: 1.4;
    color: var(--ink-soft);
  }
  .contact .company { font-weight: 700; color: var(--ink); }
  .contact .gap { height: 14px; }
  .contact-line { display: flex; justify-content: flex-end; align-items: center; gap: 8px; }
  .contact-line svg { width: 13px; height: 13px; fill: var(--ink); flex: none; }
  .model-block {
    position: absolute;
    left: 46px;
    bottom: 36px;
  }
  .card--front .brand { font-size: 38px; margin-bottom: 8px; }
  .model-specs {
    margin-left: 70px;
    font-size: 22px;
    line-height: 1.2;
    color: var(--ink);
  }
</style>
</head>
<body>

<section class="card card--back">
  <div class="rifle-photo" role="img" aria-label="Photo of a custom AR rifle with scope and suppressor"></div>
  <div class="back-content">
    <div class="brand"><span class="brand-mark"></span>KT DESIGN</div>
    <ul class="features">
      <li>Custom AR's built correctly</li>
      <li>All rifles come with honed uppers &amp; bedded barrels</li>
      <li>All rifles are fully tested &amp; come with a 3 shot card</li>
      <li>Law Enforcement models are available</li>
      <li>Tactical Equipment Consulting</li>
      <li>One stop shop for all tactical equipment</li>
    </ul>
  </div>
</section>

<section class="card card--front">
  <div class="name-tab"></div>
  <h1 class="holder-name">BRENT HOLLIS</h1>

  <div class="contact">
    <div class="company">KT Design LLC</div>
    <div>3082 Tamblin Ct.</div>
    <div>Brookvale, TN, 29815</div>
    <div class="gap"></div>
    <div class="contact-line">(555) 614-2980
      <svg viewBox="0 0 24 24" aria-hidden="true"><path d="M6.6 10.8a15.1 15.1 0 0 0 6.6 6.6l2.2-2.2a1 1 0 0 1 1-.25 11.4 11.4 0 0 0 3.6.57 1 1 0 0 1 1 1V20a1 1 0 0 1-1 1A17 17 0 0 1 3 4a1 1 0 0 1 1-1h3.5a1 1 0 0 1 1 1c0 1.25.2 2.450.57 3.6a1 1 0 0 1-.25 1z"/></svg>
    </div>
    <div class="contact-line">brent.ktdesign@mailbriq.com
      <svg viewBox="0 0 24 24" aria-hidden="true"><path d="M2 5h20v14H2z M3.5 6.5 12 12.5l8.5-6" fill="none" stroke="#1c1c1c" stroke-width="2"/></svg>
    </div>
    <div class="contact-line">www.ktdesignrifles.com
      <svg viewBox="0 0 24 24" aria-hidden="true"><circle cx="12" cy="12" r="10"/><path d="M2 12h20M12 2c3 3 3 17 0 20M12 2c-3 3-3 17 0 20" fill="none" stroke="#fff" stroke-width="1.5"/></svg>
    </div>
  </div>

  <div class="model-block">
    <div class="brand"><span class="brand-mark"></span>KT DESIGN</div>
    <div class="model-specs">
      <div>KTD 15</div>
      <div>MULTI CAL</div>
      <div>S/N: XXXXX</div>
    </div>
  </div>
</section>

</body>
</html>
```